Software Company Business Card

We are looking for a new design of our business card. The design will also be used in the rest of our branding and marketing materials as we want to keep it all uniform. We sell POS software to fine/luxury jewelers and also offer other business services as well to help the jeweler manage their business and need something more updated, technical and fresh, preferably more on the masculine side. We do not want any designs with gems in them but if possible would like to incorporate the circle and arrow in the logo into the design, but not a requirement if you can't make it work. I would like to see a variety of the mix. The colors need to remain our blue and orange and the logo can not change. The squiggly lines have been used as our corporate identity for over 20 years and its time to update. Our company name is TELK (Superior Counter Operations Platforms).

Target Market(s)

High End Jewelers

Industry/Entity Type

Software

Contact Information for Business Card

As seen in attached image

Requirements
Must have
• Our logo and the colors must remain the same. Blue is #d95d39 and Orange is #0f5682.
Nice to have
• The circle and arrow incorporated but not a requirement.
Should not have
• Anything jewelry or gem related.

```html
<!DOCTYPE html>
<html lang="en">
<head>
<meta charset="utf-8">
<title>TELK Business Card</title>
<link href="https://fonts.googleapis.com/css2?family=Open+Sans:wght@400;700&display=swap" rel="stylesheet">
<style>
  :root {
    --brand-blue: #0f5682;
    --brand-orange: #d95d39;
    --paper: #ffffff;
    --ink-grey: #5b5f63;
    --backdrop: #d6d6d4;
  }
  * { box-sizing: border-box; margin: 0; padding: 0; }
  html, body { width: 1200px; height: 801px; overflow: hidden; }
  body {
    background: var(--backdrop);
    font-family: "Open Sans", Arial, sans-serif;
    position: relative;
  }
  .card {
    position: absolute;
    top: 246px;
    width: 540px;
    height: 309px;
    border-radius: 2px;
    box-shadow: 0 6px 18px rgba(0,0,0,0.18);
    overflow: hidden;
  }
  .card--front { left: 40px; background: var(--paper); border-bottom: 3px solid var(--brand-blue); }
  .card--back  { left: 620px; background: var(--brand-blue); }

  .company-name {
    position: absolute;
    font-weight: 700;
    font-size: 44px;
    line-height: 1;
    letter-spacing: 3px;
  }
  .card--front .company-name { left: 58px; top: 132px; color: var(--brand-blue); }
  .card--back .company-name { right: 56px; bottom: 84px; color: var(--paper); }

  .divider {
    position: absolute;
    left: 268px; top: 52px;
    width: 1.5px; height: 206px;
    background: var(--brand-blue);
  }
  .contact {
    position: absolute;
    left: 288px; top: 52px;
    color: var(--ink-grey);
    font-size: 13.5px;
    line-height: 1.45;
  }
  .contact__name {
    color: var(--brand-blue);
    font-weight: 700;
    font-size: 21px;
    line-height: 1.2;
  }
  .contact__title { margin-bottom: 10px; }
  .contact__address { margin-bottom: 10px; }
  .contact__list { list-style: none; }
  .contact__list li { display: flex; align-items: center; gap: 8px; }
  .contact__icon { width: 11px; height: 11px; flex: none; fill: var(--brand-orange); }
</style>
</head>
<body>

<section class="card card--front" aria-label="Card front">
  <p class="company-name">TELK</p>
  <div class="divider"></div>
  <div class="contact">
    <p class="contact__name">Dorian Haskell</p>
    <p class="contact__title">Director of Global Operations</p>
    <p class="contact__address">P.O. Box 418206<br>Carver, NV 89410</p>
    <ul class="contact__list">
      <li><svg class="contact__icon" viewBox="0 0 12 12"><path d="M2.5 0.5 L4.5 0.5 L5.2 3.2 L3.8 4.3 C4.5 5.8 6.2 7.5 7.7 8.2 L8.8 6.8 L11.5 7.5 L11.5 9.5 C11.5 10.7 10.7 11.5 9.5 11.5 C4.5 11 1 7.5 0.5 2.5 C0.5 1.3 1.3 0.5 2.5 0.5 Z"/></svg>800.555.0142</li>
      <li><svg class="contact__icon" viewBox="0 0 12 12"><rect x="3" y="0" width="6" height="12" rx="1.2"/><rect x="4" y="1.5" width="4" height="7" fill="#fff"/></svg>702.555.0187</li>
      <li><svg class="contact__icon" viewBox="0 0 12 12"><rect x="0" y="2" width="12" height="8" rx="1"/><path d="M0.5 2.5 L6 7 L11.5 2.5" stroke="#fff" stroke-width="1.2" fill="none"/></svg>dorian@telkpos.com</li>
      <li><svg class="contact__icon" viewBox="0 0 12 12"><circle cx="6" cy="6" r="5.5"/><path d="M0.5 6 H11.5 M6 0.5 C3 3.5 3 8.5 6 11.5 M6 0.5 C9 3.5 9 8.5 6 11.5" stroke="#fff" stroke-width="0.9" fill="none"/></svg>www.telkpos.com</li>
    </ul>
  </div>
</section>

<section class="card card--back" role="img" aria-label="Card back, blue field where a repeating embossed emblem pattern sits">
  <p class="company-name">TELK</p>
</section>

</body>
</html>
```